Industrial automation company needs new business cards

We need a new business card designed. We have an existing logo that is very simple and are happy to consider changes to it. We have been in business for more than 10 years and our logo has some brand recognition.
We are a company of engineers and build systems for industrial automation, substation automation, power and energy monitoring and production data vertical integration. Our main clients are food manufacturers, data centers and government establishments.
Our current business cards have our name, qualifications, job title, telephone, email and web address details. We don't need our physical address on our business cards. I've attached our current logo

Industry/Entity Type

Business

Logo Text

varlo

Font styles to use
Sans Serif

Colors
6b449b

Requirements
Must have
• - double sided business cards
• - name (eg Hello There)
• - qualifications (BE Elec MIRQT)
• - job title (eg Senior Engineer)
• - telephone (eg 0400 000 000)
• - email (eg hello.there@varlo.com.au)
• - web address (eg varlo.com.au)
Nice to have
• include our target markets on the back side of the card
• - industrial automation
• - substation automation
• - power and energy monitoring
• - production data vertical integration

```html
<!DOCTYPE html>
<html lang="en">
<head>
<meta charset="utf-8">
<title>Varlo business cards</title>
<link rel="stylesheet" href="https://fonts.googleapis.com/css2?family=Roboto:wght@400;700&display=swap">
<style>
  :root {
    --violet: #7a0ff0;
    --violet-mid: #6200cc;
    --violet-deep: #4a0094;
    --ink-dark: #3a0080;
    --grey-text: #444444;
    --wordmark-grey: #555555;
    --paper: #e6e6e6;
    --top-bg: #f4f4f4;
    --stage-bg: #161616;
  }
  * { margin: 0; padding: 0; box-sizing: border-box; }
  html, body { width: 1200px; height: 1120px; overflow: hidden; }
  body { font-family: "Roboto", Arial, sans-serif; background: var(--stage-bg); position: relative; }

  .brand-panel {
    position: absolute; left: 0; top: 0; width: 1200px; height: 350px;
    background: var(--top-bg);
    display: flex; align-items: center; justify-content: center;
  }
  .wordmark {
    display: flex; align-items: center; gap: 14px;
    font-weight: 700; text-transform: uppercase; letter-spacing: 6px;
  }
  .wordmark .dot { width: 22px; height: 22px; background: var(--violet); }
  .brand-panel .wordmark { font-size: 56px; color: var(--wordmark-grey); }

  .card {
    position: absolute; top: 630px; width: 461px; height: 257px;
    box-shadow: 0 6px 14px rgba(0,0,0,.6);
    overflow: hidden;
  }
  .card-front { left: 120px; background: var(--paper); }
  .card-back { left: 621px; }

  .front-band { position: absolute; left: 0; top: 0; width: 120px; height: 257px; }
  .card-front .wordmark {
    position: absolute; left: 108px; top: 150px;
    font-size: 26px; color: var(--grey-text); letter-spacing: 3px; gap: 8px;
  }
  .card-front .wordmark .dot { width: 12px; height: 12px; }

  .contact { position: absolute; left: 275px; top: 82px; color: var(--grey-text); font-size: 12px; line-height: 16px; }
  .contact .name { color: var(--violet); font-size: 16px; font-weight: 700; line-height: 20px; text-transform: uppercase; }
  .contact .lines { margin-top: 0; }
  .contact .details { margin-top: 13px; list-style: none; }
  .contact .details li { display: flex; align-items: center; gap: 8px; }
  .contact .details svg { width: 11px; height: 11px; flex: none; }

  .back-fill { position: absolute; inset: 0; }
  .card-back .wordmark {
    position: absolute; right: 32px; bottom: 26px;
    font-size: 30px; color: var(--ink-dark); letter-spacing: 4px;
  }
  .card-back .wordmark .dot { width: 14px; height: 14px; background: var(--ink-dark); }
</style>
</head>
<body>
  <section class="brand-panel">
    <div class="wordmark"><span class="dot"></span><span>varlo</span></div>
  </section>

  <article class="card card-front">
    <svg class="front-band" viewBox="0 0 120 257" role="img" aria-label="Faceted violet band with a notched edge">
      <defs>
        <linearGradient id="bandTone" x1="0" y1="0" x2="1" y2="1">
          <stop offset="0" stop-color="#5a00b8"/>
          <stop offset="1" stop-color="#7a0ff0"/>
        </linearGradient>
      </defs>
      <polygon points="0,0 86,0 113,48 103,66 113,84 62,172 111,257 0,257" fill="url(#bandTone)"/>
    </svg>
    <div class="wordmark"><span class="dot"></span><span>varlo</span></div>
    <div class="contact">
      <div class="name">Jamie Corlett</div>
      <div class="lines">BE Elec MIRQT<br>Senior Engineer</div>
      <ul class="details">
        <li><svg viewBox="0 0 12 12"><path d="M3 1 L5 3.5 L4 5 Q5.5 7.5 7 8 L8.5 7 L11 9 L9.5 11 Q3 10 1 2.5 Z" fill="#7a0ff0"/></svg>+61 2 5550 1284</li>
        <li><svg viewBox="0 0 12 12"><rect x="1" y="2.5" width="10" height="7" fill="#7a0ff0"/><path d="M1 2.5 L6 7 L11 2.5" stroke="#e6e6e6" fill="none"/></svg>jamie@varlo.com.au</li>
        <li><svg viewBox="0 0 12 12" fill="none" stroke="#7a0ff0" stroke-width="1"><circle cx="6" cy="6" r="5"/><ellipse cx="6" cy="6" rx="2.2" ry="5"/><path d="M1 6 H11 M2 3.5 H10 M2 8.5 H10"/></svg>www.varlo.com.au</li>
      </ul>
    </div>
  </article>

  <article class="card card-back">
    <svg class="back-fill" viewBox="0 0 461 257" preserveAspectRatio="none" role="img" aria-label="Faceted violet geometric surface">
      <defs>
        <linearGradient id="backTone" x1="0" y1="0" x2="1" y2="1">
          <stop offset="0" stop-color="#4a0094"/>
          <stop offset="0.5" stop-color="#6a00dd"/>
          <stop offset="1" stop-color="#7a0ff0"/>
        </linearGradient>
      </defs>
      <rect width="461" height="257" fill="url(#backTone)"/>
    </svg>
    <div class="wordmark"><span class="dot"></span><span>varlo</span></div>
  </article>
</body>
</html>
```